Business Card, Stationary with Shark Logo for Personal Injury Lawyer

I need business cards and stationery with a shark logo for my Personal Injury Law Practice. Has to have this written on it:
Martin K. Holloway
Injury Lawyer
The Copperfield Building
718 Wexley Street
Providence, Rhode Island 02908
401-555-0172
Martinholloway.example

Contact Information for Business Card

Martin K. Holloway, Injury Lawyer, address, 401-555-0172, martinholloway.example

```html
<!DOCTYPE html>
<html lang="en">
<head>
<meta charset="utf-8">
<title>Martin K. Holloway — Business Card</title>
<link href="https://fonts.googleapis.com/css2?family=Roboto:wght@400;700;900&display=swap" rel="stylesheet">
<style>
  :root {
    --backdrop: #e6e8eb;
    --navy: #2a2461;
    --card-light: #f1f4f7;
    --ink-grey: #5a5a60;
    --white: #ffffff;
  }
  * { box-sizing: border-box; margin: 0; padding: 0; }
  html, body { width: 1200px; height: 900px; overflow: hidden; }
  body {
    background: var(--backdrop);
    font-family: "Roboto", Arial, sans-serif;
    position: relative;
  }
  .card {
    position: absolute;
    left: 363px;
    width: 475px;
    height: 271px;
  }
  .card--front { top: 145px; background: var(--navy); display: flex; align-items: center; justify-content: center; }
  .card--back { top: 484px; background: var(--card-light); }

  .wordmark {
    font-weight: 900;
    text-transform: uppercase;
    text-align: center;
    line-height: 1;
    letter-spacing: 0.5px;
  }
  .card--front .wordmark { color: var(--white); font-size: 40px; }
  .card--back .wordmark {
    position: absolute;
    left: 48px; top: 96px; width: 160px;
    color: var(--navy); font-size: 26px;
  }
  .wordmark span { display: block; }

  .divider {
    position: absolute;
    left: 237px; top: 71px;
    width: 1px; height: 127px;
    background: var(--navy);
  }
  .contact {
    position: absolute;
    left: 266px; top: 67px;
    color: var(--ink-grey);
    font-size: 11px;
    line-height: 15px;
  }
  .contact__name { color: var(--navy); font-weight: 700; font-size: 14.5px; line-height: 18px; text-transform: uppercase; }
  .contact__title { margin-bottom: 13px; }
  .contact__address { margin-bottom: 12px; }
  .contact__line { display: flex; align-items: center; gap: 6px; }
  .contact__line svg { width: 10px; height: 10px; fill: var(--navy); flex: none; }
</style>
</head>
<body>
  <section class="card card--front">
    <div class="wordmark"><span>Martin K.</span><span>Holloway</span></div>
  </section>

  <section class="card card--back">
    <div class="wordmark"><span>Martin K.</span><span>Holloway</span></div>
    <div class="divider"></div>
    <div class="contact">
      <p class="contact__name">Martin K. Holloway</p>
      <p class="contact__title">Injury Lawyer</p>
      <p class="contact__address">The Copperfield Building<br>718 Wexley Street<br>Providence, Rhode Island 02908</p>
      <p class="contact__line">
        <svg viewBox="0 0 24 24" aria-hidden="true"><path d="M6.6 10.8a15.1 15.1 0 0 0 6.6 6.6l2.2-2.2c.3-.3.7-.4 1-.2 1.1.4 2.3.6 3.6.6.6 0 1 .4 1 1V20c0 .6-.4 1-1 1A17 17 0 0 1 3 4c0-.6.4-1 1-1h3.5c.6 0 1 .4 1 1 0 1.3.2 2.5.6 3.6.1.3 0 .7-.2 1z"/></svg>
        401-555-0172
      </p>
      <p class="contact__line">
        <svg viewBox="0 0 24 24" aria-hidden="true"><path d="M12 2a10 10 0 1 0 0 20 10 10 0 0 0 0-20zm6.9 6h-2.9a15.7 15.7 0 0 0-1.4-3.6A8 8 0 0 1 18.9 8zM12 4c.8 1.2 1.5 2.5 1.9 4h-3.8c.4-1.5 1.1-2.8 1.9-4zM4.3 14a8.2 8.2 0 0 1 0-4h3.4a16.5 16.5 0 0 0 0 4zm.8 2h2.9c.3 1.3.8 2.5 1.4 3.6A8 8 0 0 1 5.1 16zM8 8H5.1a8 8 0 0 1 4.3-3.6C8.8 5.5 8.3 6.7 8 8zm4 12c-.8-1.2-1.5-2.5-1.9-4h3.8c-.4 1.5-1.1 2.8-1.9 4zm2.3-6H9.7a14.7 14.7 0 0 1 0-4h4.6a14.7 14.7 0 0 1 0 4zm.3 5.6c.6-1.1 1.1-2.3 1.4-3.6h2.9a8 8 0 0 1-4.3 3.6zm1.7-5.6a16.5 16.5 0 0 0 0-4h3.4a8.2 8.2 0 0 1 0 4z"/></svg>
        Martinholloway.example
      </p>
    </div>
  </section>
</body>
</html>
```